Need Business Card Design, Letterhead and a Basic Form layout based on Existing Logo

We need (1) a business card design, (2) a letterhead design and (3) a basic form layout for an international holding company. This holding company has just formed two (2) sub-companies. The logo is the same for each company with only a simple word change for each company. The business card, letterhead and form design will be essentially the same for each company... with only the one word change being different.
The names of the companies are as follows:
1. Kestrel Trust Services
2. Kestrel Immigration Services
The design for the business card, letterhead and Form must be strong, clean and classy.
Our clients will be older, wealthy and mostly Asian. The design must project strength, stability and confidence.
The card may contain the following data:
1. The Logo
2. The name of the person
3. The title of the person
4. The address of the company
5. The Company Phone number
6. The personal mobile number
7. The Skype number (VOIP)
8. The WICKR number (IM)
9. The email
10. The website
We will attach AI files of our logo for the "Kestrel Trust Services" company in the colors Black/White and Blue in both Horizontal and Vertical format... We have also included separate files of the logo icon.
We uploaded the AI files to give the designer the maximum options regarding color and effects. We included the separate files for the icon because we would like to give the designer the option of a watermark. Also, we think it might be nice to highlight the icon on the back of the card perhaps with the website address.
We are not sure which colors or color combinations would be best for these two companies. We know the colors must again project strength, stability and confidence. Perhaps, a combination that might include Tan, Black and White... not sure... need design help... remember this has to have the presence of a bank-like institution... no cartoonish designs or flashy color combinations... please.
The basic form layout will be used for various questionaires, input sheets and instructions.... etc.
NOTE: The fonts used in the logo are Trajan Pro Bold for word "KESTREL" and Trajan Pro Regular for "XXXXXXXXX SERVICES".

```html
<!DOCTYPE html>
<html lang="en">
<head>
<meta charset="utf-8">
<title>Kestrel Trust Services — Stationery</title>
<link href="https://fonts.googleapis.com/css2?family=Cinzel:wght@400;700&family=Questrial&display=swap" rel="stylesheet">
<style>
  :root{
    --backdrop:#8c8c8c;
    --ink:#1e1a1a;
    --paper:#ffffff;
    --night:#0b0b0c;
    --night-2:#1c1d20;
    --silver-light:#f2f2f2;
    --silver-mid:#9a9a9a;
    --muted:#a9a9a9;
    --watermark:#e2e2e2;
  }
  *{box-sizing:border-box;margin:0;padding:0}
  html,body{width:1200px;height:766px;overflow:hidden;background:var(--backdrop)}
  .sheet{position:relative;width:1200px;height:766px}

  .brand{position:absolute;display:flex;align-items:center;gap:18px}
  .brand-mark{width:60px;height:60px;background:var(--ink)}
  .brand-name{font-family:"Cinzel",serif;color:var(--ink);font-weight:400;line-height:1}
  .brand-name .primary,.brand-name .secondary{display:block}

  /* card back */
  .card-back{position:absolute;left:46px;top:38px;width:563px;height:328px;overflow:hidden;
    background:radial-gradient(ellipse at 50% 20%,var(--night-2) 0%,var(--night) 70%)}
  .card-back .watermark{position:absolute;left:180px;top:40px;width:220px;height:220px;
    border:2px solid rgba(255,255,255,.05);background:rgba(255,255,255,.015)}
  .card-back .site{position:absolute;left:0;right:0;top:152px;text-align:center;
    font-family:"Questrial",sans-serif;font-size:20px;letter-spacing:6.4px;
    background:linear-gradient(180deg,#ffffff 0%,#b5b5b5 100%);-webkit-background-clip:text;background-clip:text;color:transparent}

  /* card front */
  .card-front{position:absolute;left:45px;top:403px;width:565px;height:330px;overflow:hidden;background:var(--paper)}
  .card-front .brand{left:36px;top:48px}
  .card-front .brand-mark{width:66px;height:66px}
  .card-front .primary{font-size:36px;font-weight:400;letter-spacing:1px}
  .card-front .secondary{font-size:20px;margin-top:4px;margin-left:2px}
  .silver-band{position:absolute;left:0;right:0;height:14px;
    background:linear-gradient(90deg,var(--silver-mid) 0%,var(--silver-light) 45%,#cfcfcf 70%,var(--silver-mid) 100%)}
  .card-front .silver-band{top:156px}
  .card-front .dark-panel{position:absolute;left:0;right:0;top:170px;bottom:0;
    background:linear-gradient(180deg,#242527 0%,var(--night) 100%)}
  .holder{position:absolute;right:407px;top:12px;text-align:right;font-family:"Questrial",sans-serif}
  .holder .name{color:var(--muted);font-size:18px}
  .holder .title{color:#fff;font-size:15px;margin-top:3px}
  .divider{position:absolute;left:174px;top:10px;width:1px;height:124px;background:#8a8a8a}
  .contacts{position:absolute;left:188px;top:8px;list-style:none;font-family:"Questrial",sans-serif;color:#fff;font-size:14.5px;line-height:18.4px}
  .contacts li{display:flex;align-items:flex-start;gap:4px}
  .contacts svg{width:13px;height:13px;margin-top:2px;flex:none;fill:#ccc}

  /* letterhead */
  .letterhead{position:absolute;left:645px;top:38px;width:538px;height:695px;overflow:hidden;background:var(--paper)}
  .letterhead .brand{left:15px;top:16px;gap:34px}
  .letterhead .brand-mark{width:66px;height:66px}
  .letterhead .primary{font-size:32px;letter-spacing:1px}
  .letterhead .secondary{font-size:18px;margin-top:2px}
  .letterhead .watermark{position:absolute;left:300px;top:290px;width:300px;height:300px;background:var(--watermark)}
  .letterhead .silver-band{top:622px;height:6px}
  .letterhead .dark-panel{position:absolute;left:0;right:0;top:628px;bottom:0;
    background:linear-gradient(180deg,#1e1f21 0%,var(--night) 100%)}
  .letterhead .contacts{left:6px;top:8px;font-size:6.2px;line-height:7.6px}
  .letterhead .contacts svg{width:6px;height:6px;margin-top:1px}
</style>
</head>
<body>
<main class="sheet">

  <section class="card-back" aria-label="Business card back">
    <div class="watermark"></div>
    <p class="site">www.kestreltrust.com</p>
  </section>

  <section class="card-front" aria-label="Business card front">
    <div class="brand">
      <span class="brand-mark"></span>
      <h1 class="brand-name"><span class="primary">KESTREL</span><span class="secondary">Trust Services</span></h1>
    </div>
    <div class="silver-band"></div>
    <div class="dark-panel">
      <div class="holder">
        <p class="name">Mara Ellison</p>
        <p class="title">Manager</p>
      </div>
      <span class="divider"></span>
      <ul class="contacts">
        <li><svg viewBox="0 0 12 12"><rect x="3" y="0.5" width="6" height="11" rx="1"/></svg>555-013-2847</li>
        <li><svg viewBox="0 0 12 12"><path d="M2 1l2.5 0 1 3-1.5 1a7 7 0 0 0 3 3l1-1.5 3 1V10a1.5 1.5 0 0 1-1.5 1.5A9 9 0 0 1 .5 2.5 1.5 1.5 0 0 1 2 1z"/></svg>555-014-6620</li>
        <li><svg viewBox="0 0 12 12"><circle cx="6" cy="6" r="5.5"/></svg>ellison-kestreltrust</li>
        <li><svg viewBox="0 0 12 12"><path d="M0.5 2.5h11v7h-11z M0.5 2.5l5.5 4 5.5-4" fill="none" stroke="#ccc" stroke-width="1.2"/></svg>info@kestreltrust.com</li>
        <li><svg viewBox="0 0 12 12"><g fill="none" stroke="#ccc" stroke-width="1"><circle cx="6" cy="6" r="5.2"/><ellipse cx="6" cy="6" rx="2.2" ry="5.2"/><path d="M.8 6h10.4"/></g></svg>www.kestreltrust.com</li>
        <li><svg viewBox="0 0 12 12"><path d="M6 .8L.5 5.8h1.6v5.4h3V8h1.8v3.2h3V5.8h1.6z"/></svg>4870 N. Ridgeline Road,<br>Aldermoor, CO 80911</li>
      </ul>
    </div>
  </section>

  <section class="letterhead" aria-label="Letterhead">
    <div class="brand">
      <span class="brand-mark"></span>
      <h2 class="brand-name"><span class="primary">KESTREL</span><span class="secondary">Trust Services</span></h2>
    </div>
    <div class="watermark"></div>
    <div class="silver-band"></div>
    <footer class="dark-panel">
      <ul class="contacts">
        <li><svg viewBox="0 0 12 12"><rect x="3" y="0.5" width="6" height="11" rx="1"/></svg>555-013-2847</li>
        <li><svg viewBox="0 0 12 12"><path d="M2 1l2.5 0 1 3-1.5 1a7 7 0 0 0 3 3l1-1.5 3 1V10a1.5 1.5 0 0 1-1.5 1.5A9 9 0 0 1 .5 2.5 1.5 1.5 0 0 1 2 1z"/></svg>555-014-6620</li>
        <li><svg viewBox="0 0 12 12"><circle cx="6" cy="6" r="5.5"/></svg>ellison-kestreltrust</li>
        <li><svg viewBox="0 0 12 12"><path d="M0.5 2.5h11v7h-11z"/></svg>info@kestreltrust.com</li>
        <li><svg viewBox="0 0 12 12"><circle cx="6" cy="6" r="5.2"/></svg>www.kestreltrust.com</li>
        <li><svg viewBox="0 0 12 12"><path d="M6 .8L.5 5.8h1.6v5.4h7.8V5.8h1.6z"/></svg>4870 N. Ridgeline Road,<br>Aldermoor, CO 80911</li>
      </ul>
    </footer>
  </section>

</main>
</body>
</html>
```